Wine Label for a wine from Tuscany, Italy

We need a wine label for a white and red wine, can be the same label or can be somewhat differentiated with any variation you feel would be good.. These two wines come from Tuscany, Italy. Wine labels from Tuscany Italy tend to be traditional. We are open to traditional looking labels but also more modern, eye catching too. We want to convey a sense of elegance, importance, great wine. I am attaching some examples of labels we like from Tuscany, also a label that was designed for us recently by one of you, which we LOVE. No wine glasses, wine bottles or grapes featured on the label please. We tend to like the white background. No blue please.

Target Market(s)

More women than men purchase wine, but it needs to appeal to both sexes.

Requirements
Must have
• Wine Name: Casa Morel or Casa morel
• Type/Varletal: Rosso Toscano (White is Vermentino)
• Vintage (year): 2018
• That is all the text we want on the label, thanks
Nice to have
• Clean, something that makes someone want to grab this wine bottle off the shelf!
Should not have
• Images of Wine glass, wine bottles, grapes
• Do not use the color blue please.

```html
<!DOCTYPE html>
<html lang="en">
<head>
<meta charset="utf-8">
<title>Casa Morel – Rosso Toscano Label</title>
<link rel="stylesheet" href="https://fonts.googleapis.com/css2?family=Josefin+Sans:wght@300&family=Great+Vibes&display=swap">
<style>
  :root {
    --backdrop: #e9e6e2;
    --label-white: #ffffff;
    --label-shade: #f3f3f3;
    --ink: #1a1a1a;
    --ink-soft: #333333;
    --copper-dark: #7a3a1a;
    --copper: #b8652e;
    --copper-light: #e49a5e;
  }
  * { margin: 0; padding: 0; box-sizing: border-box; }
  html, body {
    width: 1200px;
    height: 960px;
    overflow: hidden;
    background: var(--backdrop);
  }
  .canvas {
    position: relative;
    width: 1200px;
    height: 960px;
    display: flex;
    align-items: center;
    justify-content: center;
  }
  .wine-label {
    position: relative;
    width: 640px;
    height: 680px;
    background: radial-gradient(ellipse at 50% 40%, var(--label-white) 55%, var(--label-shade) 100%);
    box-shadow: 0 6px 24px rgba(0,0,0,0.12);
    text-align: center;
    color: var(--ink);
  }
  .copper-rule {
    position: absolute;
    left: 0;
    right: 0;
    top: 34px;
    height: 7px;
    background: linear-gradient(90deg, var(--copper-dark), var(--copper) 30%, var(--copper-light) 55%, var(--copper) 75%, var(--copper-dark));
  }
  .wine-name {
    position: absolute;
    top: 180px;
    left: 0;
    right: 0;
    font-family: "Josefin Sans", sans-serif;
    font-weight: 300;
    font-size: 74px;
    letter-spacing: 2px;
    color: var(--ink);
  }
  .varietal {
    position: absolute;
    top: 395px;
    left: 0;
    right: 0;
    line-height: 1.15;
  }
  .script {
    font-family: "Great Vibes", cursive;
    font-size: 27px;
    color: var(--ink);
  }
  .varietal-note {
    font-family: "Josefin Sans", sans-serif;
    font-weight: 300;
    font-size: 17px;
    color: var(--ink-soft);
    margin-top: 4px;
  }
  .vintage {
    position: absolute;
    top: 555px;
    left: 0;
    right: 0;
    line-height: 1.1;
  }
  .vintage .script { font-size: 22px; }
  .vintage-year {
    font-family: "Great Vibes", cursive;
    font-size: 24px;
  }
</style>
</head>
<body>
  <main class="canvas">
    <section class="wine-label">
      <div class="copper-rule"></div>
      <h1 class="wine-name">Casa Morel</h1>
      <div class="varietal">
        <p class="script">Type/Varletal:</p>
        <p class="script">Rosso Toscano</p>
        <p class="varietal-note">(White é Vermentino)</p>
      </div>
      <div class="vintage">
        <p class="script">Vintage (year)</p>
        <p class="vintage-year">2018</p>
      </div>
    </section>
  </main>
</body>
</html>
```